Design extract to a timeless cook-book with a modern look.

Hi,

(This is no bookcover-design.)

I need help with a book design - a few pages that will go as a proposal to a publishing company.

The project has three segments.
1. One is the story of the person behind it (its a sad story that ends well - I have replaced it with Lorem Ipsum) and,
2. the second is a cookery-segment with recipe and,
3. lastly a table of contents for the same.

The right order in the book would be to start with:
1. Table of contents (I upload two files - the one in Swedish is the one to choose. The other is for you to know what it is)
2. The story. The Lorem Ipsum text.
3. Lastly the main part - cooking-recipe. Here you see boxes with one line of text for a future picture. You can just think about the leave space, for a later inserted picture.

Would like a modern look - but still a touch of a classic cookery-book. Please give examples of page layout in the three segments. Also think about the design of the books figures in the corner. Feel free to act upon it.
I am sorry Im in a hurry with this project - but please do not come back with a proposal made in 15 min. It will not go thru.

You are mostly welcome to ask me questions. Good luck!

Target Market(s)

Adults - intrested in cooking.

Industry/Entity Type

It Company

Font styles to use
Serif
Sans Serif
Script

Colors

Designer to choose colors to be used in the design.

Requirements
Must have
• The feeling of a cook-book. Easy to read. Format printed will be (or around) A4 (210 x 297 mm.)
• - All three segments.

```html
<!DOCTYPE html>
<html lang="sv">
<head>
<meta charset="utf-8">
<title>Kokbok – uppslag</title>
<link rel="stylesheet" href="https://fonts.googleapis.com/css2?family=Jost:wght@400;500;600;700&family=Tinos:ital,wght@0,400;0,700;1,400&family=Questrial&display=swap">
<style>
  :root{
    --board:#b8922b;
    --paper:#ffffff;
    --ink:#111111;
    --muted:#7a7a7a;
    --rule:#222222;
    --block:#000000;
    --photo-a:#efe6d8;
    --photo-b:#c94a2c;
    --photo-c:#8a3a1e;
  }
  *{box-sizing:border-box;margin:0;padding:0}
  html,body{width:1200px;height:2436px;overflow:hidden}
  body{background:var(--board);position:relative;font-family:"Tinos",serif;color:var(--ink)}
  .page{position:absolute;background:var(--paper);width:543px;height:768px;overflow:hidden}
  .p-toc{left:29px;top:25px}
  .p-menu{left:615px;top:25px}
  .p-story{left:29px;top:821px}
  .p-ketchup{left:615px;top:821px}
  .p-photo{left:29px;top:1619px;height:793px}

  .page-title{position:absolute;left:33px;top:34px;font-family:"Jost",sans-serif;font-weight:700;font-size:17px;letter-spacing:.3px}
  .folio{position:absolute;right:33px;bottom:14px;font-family:"Jost",sans-serif;font-weight:700;font-size:9px;letter-spacing:.3px}

  /* Innehåll */
  .toc{position:absolute;left:33px;top:160px;width:237px}
  .toc-section{border-top:1.3px solid var(--rule);padding-top:4px}
  .toc-head{font-family:"Jost",sans-serif;font-weight:700;font-size:12.5px;border-bottom:1px solid var(--rule);padding-bottom:6px}
  .toc-row{display:flex;justify-content:space-between;font-size:9px;padding:9px 0 13px}
  .toc-row b{font-family:"Jost",sans-serif;font-size:10px}

  /* Receptdelen */
  .week{position:absolute;top:191px;width:232px}
  .week-a{left:33px}.week-b{left:276px}
  .week-head{border-top:1.3px solid var(--rule);border-bottom:1px solid var(--rule);font-family:"Jost",sans-serif;font-weight:700;font-size:11px;padding:4px 0 5px}
  .week-sub{display:flex;justify-content:space-between;border-bottom:1px solid var(--rule);font-family:"Jost",sans-serif;font-weight:700;font-size:10px;padding:8px 0 7px;margin-bottom:14px}
  .week-sub span{font-family:"Tinos",serif;font-weight:400;font-size:10px;letter-spacing:.5px}
  .week-sub span b{font-family:"Jost",sans-serif;margin-left:8px}
  .day{margin-bottom:13px}
  .day-name{font-family:"Jost",sans-serif;font-weight:600;font-size:10.5px;line-height:1.1}
  .day-dish{display:flex;justify-content:space-between;align-items:flex-end;font-size:9px;line-height:1.35}
  .day-dish b{font-family:"Jost",sans-serif;font-size:10px}
  .day-dish .indent{display:block;padding-left:30px}
  .footnote{font-family:"Jost",sans-serif;font-size:7.5px;padding-left:32px;margin-top:-2px}

  /* Berättelse */
  .story-col{position:absolute;top:165px;width:234px;font-size:7.6px;line-height:11.7px;text-align:justify;overflow:hidden}
  .story-col p+p{text-indent:14px}
  .col-1{left:33px;height:570px}
  .col-2{left:278px;height:334px}
  .picture-box{position:absolute;left:278px;top:508px;width:232px;height:228px;background:var(--block);color:#fff;display:flex;align-items:center;justify-content:center;font-family:"Jost",sans-serif;font-size:17px}

  /* Ketchup */
  .intro{position:absolute;top:170px;width:232px;font-family:"Jost",sans-serif;font-weight:700;font-size:7.2px;line-height:9.6px}
  .intro p+p{margin-top:9px}
  .intro-a{left:33px}.intro-b{left:276px}
  .recipe-title{position:absolute;left:33px;top:421px;font-family:"Jost",sans-serif;font-weight:700;font-size:16.5px;letter-spacing:.2px}
  .recipe-label{font-family:"Jost",sans-serif;font-weight:700;font-size:10px;margin-bottom:12px}
  .ingredients{position:absolute;left:33px;top:483px;width:230px}
  .ingredients li{list-style:none;font-family:"Questrial",sans-serif;font-size:9.5px;color:#555;line-height:12px;margin-bottom:5px}
  .ingredients li .indent{padding-left:26px;display:block}
  .method{position:absolute;left:276px;top:483px;width:235px}
  .method ol{padding-left:14px}
  .method li{font-size:9.2px;line-height:11.5px;margin-bottom:7px;padding-left:2px}
  .method li::marker{font-family:"Jost",sans-serif;font-weight:700}
  .serve-note{font-size:9.2px;line-height:11.5px;color:var(--muted);margin-top:8px}

  /* Foto */
  .dish-photo{position:absolute;left:33px;top:33px;width:477px;height:729px;
    background:linear-gradient(180deg,var(--photo-a) 0%,#e8d9c2 24%,#f6f3ee 38%,var(--photo-b) 62%,var(--photo-c) 78%,#f1ede6 92%,#6e7a4a 100%)}
</style>
</head>
<body>

<section class="page p-toc">
  <h1 class="page-title">INNEHÅLL</h1>
  <div class="toc">
    <div class="toc-section">
      <div class="toc-head">BAKGRUND:</div>
      <div class="toc-row"><span>Hur boken kom till</span><b>2</b></div>
    </div>
    <div class="toc-section">
      <div class="toc-head">FRUKOST OCH MELLANMÅL:</div>
      <div class="toc-row"><span>Tips på sidana</span><b>4</b></div>
    </div>
    <div class="toc-section">
      <div class="toc-head">VECKOMATSEDLAR:</div>
      <div class="toc-row"><span>4 stycken med lunch och kvällsmål</span><b>6</b></div>
    </div>
  </div>
</section>

<section class="page p-menu">
  <div class="week week-a">
    <div class="week-head">RECEPTDELEN INLEDNING</div>
    <div class="week-sub">LUNCHRECEPT<span>VECKA<b>1</b></span></div>
    <div class="day"><div class="day-name">Måndag:</div><div class="day-dish"><span>Korvrecept vecka 1</span><b>4</b></div></div>
    <div class="day"><div class="day-name">Tisdag:</div><div class="day-dish"><span>Vegetariskt vecka 1</span><b>4</b></div></div>
    <div class="day"><div class="day-name">Onsdag:</div><div class="day-dish"><span>Fisk vecka 1</span><b>4</b></div></div>
    <div class="day"><div class="day-name">Torsdag:</div><div class="day-dish"><span>Vegetariskt vecka 1</span><b>4</b></div></div>
    <div class="day"><div class="day-name">Fredag:</div><div class="day-dish"><span>Enkel och billig köttfärssås och pasta</span><b>4*</b></div></div>
    <div class="day"><div class="day-name">Lördag:</div><div class="day-dish"><span>Brunch vecka 1 en smörgås kan vara<span class="indent">som en hel måltid</span></span><b>4</b></div></div>
    <div class="day"><div class="day-name">Söndag:</div><div class="day-dish"><span>Brunch vecka 1 med fokus på ägg</span><b>4</b></div></div>
    <div class="footnote">* Se dessa sidor i separata bilagor</div>
  </div>
  <div class="week week-b">
    <div class="week-head">RECEPTDELEN INLEDNING</div>
    <div class="week-sub">LUNCHRECEPT<span>VECKA<b>2</b></span></div>
    <div class="day"><div class="day-name">Måndag:</div><div class="day-dish"><span>korvrecept vecka 2</span><b>4</b></div></div>
    <div class="day"><div class="day-name">Tisdag:</div><div class="day-dish"><span>vegetariskt vecka 2</span><b>4</b></div></div>
    <div class="day"><div class="day-name">Onsdag:</div><div class="day-dish"><span>fisk vecka 2</span><b>4</b></div></div>
    <div class="day"><div class="day-name">Torsdag:</div><div class="day-dish"><span>vegetariskt vecka 2</span><b>4</b></div></div>
    <div class="day"><div class="day-name">Fredag:</div><div class="day-dish"><span>köttfärsrätt vecka 2</span><b>4*</b></div></div>
    <div class="day"><div class="day-name">Lördag:</div><div class="day-dish"><span>Brunch vecka 2 en smörgås kan vara<span class="indent">som en hel måltid</span></span><b>4</b></div></div>
    <div class="day"><div class="day-name">Söndag:</div><div class="day-dish"><span>Brunch vecka 2 med fokus på ägg</span><b>4</b></div></div>
  </div>
</section>

<section class="page p-story">
  <h1 class="page-title">1 SEPTEMBER 2013</h1>
  <div class="story-col col-1">
    <p>Lorem ipsum dolor sit amet, consectetur adipiscing elit. Praesent sollicitudin turpis ipsum, id venenatis libero elementum quis. Quisque molestie ullamcorper mauris, sed tempor ante pharetra eget. Integer eu mi pulvinar, imperdiet justo sed, semper lacus. Vestibulum ultrices turpis massa, aliquet egestas tortor fermentum vitae. Phasellus et malesuada ipsum, id consequat eros. Vestibulum mattis volutpat ex. Proin sit amet erat non sem convallis suscipit a sollicitudin purus. Sed malesuada ligula eget nibh sodales, ut egestas felis fringilla. Proin rhoncus enim ut arcu placerat, ac sagittis turpis ultrices. Sed imperdiet semper urna quis volutpat. Aenean non nisl laoreet, congue lorem vitae, lobortis turpis. Praesent non consectetur lectus. Cras ultricies ornare maximus. Curabitur et nisi eget mi pharetra auctor eget sed nibh. Praesent imperdiet ipsum non dui vehicula lobortis.</p>
    <p>Ut at quam in elit ultrices tempus in id urna. Vestibulum ac porttitor libero, sed bibendum lacus. Curabitur volutpat orci ultrices lectus laoreet posuere. Donec et libero tortor. Maecenas nisl tellus, tempus id lorem blandit, tempus porttitor purus. Sed in urna neque. Nulla facilisi. Mauris ut tortor at ipsum convallis elementum. Morbi rhoncus felis non nibh molestie, a faucibus sem fringilla. Suspendisse maximus justo laoreet, feugiat eros tincidunt, egestas tortor. Etiam in nulla nisi. Fusce mi ex, porttitor in lectus ut, ultricies condimentum ligula. Cras id dapibus diam. Etiam varius volutpat velit.</p>
    <p>Ut congue nulla vitae convallis elementum. Mauris odio quam, ullamcorper in faucibus ut, luctus non tortor. Nunc eu auctor nisi. Lorem ipsum dolor sit amet, consectetur adipiscing elit. Phasellus non convallis orci. Nullam ultricies ut nibh eget molestie. Sed euismod eros vitae tellus elementum eleifend. In eu bibendum massa, sit amet fringilla libero.</p>
    <p>Curabitur non tellus turpis. Sed id commodo elit. Praesent molestie justo at sapien consectetur dictum. Etiam quis imperdiet sem. Sed iaculis sodales ex id semper. Donec a mauris purus. Integer magna justo, consectetur sit amet blandit eget, ullamcorper et dolor. Aenean dictum, felis at</p>
  </div>
  <div class="story-col col-2">
    <p>vehicula posuere, augue ante aliquet sem, eu dictum orci elit vel leo. Donec diam risus, semper ut nulla at, faucibus iaculis ante. Aliquam auctor nisi ac leo commodo vulputate. Praesent porttitor velit id ipsum sodales cursus. Curabitur eget hendrerit neque. Nullam aliquet enim nec diam mollis placerat. Lorem ipsum dolor sit amet, consectetur adipiscing elit. Sed et rhoncus nunc. Maecenas tellus elit, condimentum et consectetur a, finibus in arcu.</p>
    <p>Fusce ligula dui, tincidunt id nibh vitae, viverra consectetur magna. Aenean quis ornare sapien. Quisque tincidunt euismod semper. Maecenas ac porta nunc, quis ultricies felis. Suspendisse mollis est sed urna vulputate rutrum. Vivamus egestas tellus vitae nulla scelerisque, ut consequat lectus posuere. Praesent vitae purus id quam porttitor blandit. Donec vitae commodo nunc, vitae lacinia sapien. Quisque eu turpis nec ipsum aliquam vestibulum a vel nibh. Aliquam commodo erat in ante suscipit vehicula. Nam pretium dui non tellus venenatis rutrum. Donec feugiat erat et tortor venenatis consectetur. Nam quis molestie massa. Mauris maximus odio sit amet magna tincidunt gravida. Morbi ornare, libero ut pharetra finibus, felis ipsum laoreet quam, vitae laoreet eros ligula id nisi.</p>
  </div>
  <div class="picture-box">Picture here</div>
  <div class="folio">04 STORY</div>
</section>

<section class="page p-ketchup">
  <h1 class="page-title">TACK OCH LOV FÖR KETCHUP</h1>
  <div class="intro intro-a">
    <p>Man ska inte generalisera och rynka på näsan åt halvfabrikat och andra genvägar i köket, eller tillvaron för övrigt för den delen. Jag tillhör till exempel dem som ofta använder ketchup och det skäms jag inte för – inte nu längre.</p>
    <p>Söker man på ordet ketchup på nätet får man upp recept på hur man gör sin egen ketchup. Men varför i allsin dar ska man lägga tid på den sysslan, när det numera finns så många bra ketchupsorter med samma ingredienser som i många av recepten på "din egen" ketchup. Letar du efter en ekologisk ketchup ska du se att den ofta dessutom går att få med mindre salt och socker än den "vanliga" och dessutom kravmärkt.</p>
  </div>
  <div class="intro intro-b">
    <p>Tv-kockar och kokboksförfattare använder sällan om ens någonsin ketchup. Däremot används ofta tomatpuré, salt och socker plus något syrligt till exempel vinäger/ättika. Se där - samma ingredienser som i ketchup!</p>
    <p>I min gamla hemkunskapsbok förekommer ketchupen mer än en gång. (Kan förklaringen vara att denna smaksättare på den tiden till och med sågs som lite exotisk). Vissa av recepten i min gamla hemkunskapsbok använder jag fortfarande även om jag har ändrat en del av dem lite grann när till exempel nya kryddor har kommit ut i handeln. Köttfärssåsen på nästa uppslag har tillkommit på just det här sättet</p>
  </div>
  <h2 class="recipe-title">EXTRASNABB OCH ENKEL KÖTTFÄRSSÅS MED VALFRI PASTA</h2>
  <div class="ingredients">
    <div class="recipe-label">INGREDIENSER:</div>
    <ul>
      <li>2 hg köttfärs (valfri sort)</li>
      <li>fett att bryna i</li>
      <li>1 kartong eller burk färdig tomatsås eller<span class="indent">smaksatta krossade tomater</span></li>
      <li>150 gram valfri pasta</li>
    </ul>
  </div>
  <div class="method">
    <div class="recipe-label">TILLAGA SÅ HÄR:</div>
    <ol>
      <li>bryn köttfärsen i valfritt fett</li>
      <li>tillsätt tomatsåsen eller de krossade tomaterna och låt puttra på medelstark värme några minuter</li>
      <li>Dra nu pannan åt sidan under tiden du kokar pastan</li>
      <li>Koka pastan livligt d.v.s. på hög värme enligt anvisningen på förpackningen.</li>
      <li>Häll av vattnet från pastan och rör i köttfärssåsen i pastan.</li>
    </ol>
    <p class="serve-note">Servera någon eller några grönsaker/rotfrukter till detta. Gärna rårivna morötter och någon frusen grönsaksblandning t ex ärter, majs och paprika</p>
  </div>
  <div class="folio">05 KETCHUP</div>
</section>

<section class="page p-photo">
  <div class="dish-photo" role="img" aria-label="Foto: tallrik med fullkornspasta i tomatsås med kyckling, sparris, tomat och oliver, pastaskruvar i bakgrunden"></div>
</section>

</body>
</html>
```